Start-up company developing economical and ecological hydrogen peroxide generator needs an attractiv

We need a powerpoint design for a start-up company based in Montreal called Vorbelle currently seeking to raise funds from investors. We develop an electrochemical hydrogen peroxide generator based on new generation catalysts.

These generators allow industrial users of hydrogen peroxide to generate it onsite economically and ecologically, as opposed to buying it from the major suppliers who make it large production plants using more polluting methods and need to transport it to customers over long distances.

We would like to see designs that have a cleantech technology and green chemistry feel. Colors that evoke a sense of environmental sustainability are desired.

The final design should communicate technological innovation that makes the world a cleaner and healthier place to live.

Target Market(s)

Industrial users or producers of of hydrogen peroxide

Industry/Entity Type

It Company

Font styles to use
Sans Serif

Colors
0255a3
3276b5
85acd3
9bcb3b
add136
e3eebf

Requirements
Must have
• Clean, attractive, professional and advanced technology look.
• Our slogan is: Catalyst for innovation
Nice to have
• The cover page should have our logo and our slogan. It should also have some graphics that pertain to technology and green chemistry. The perception that one should have when looking at it is that the company is developing a clean chemical manufacturing technology that is more environmentally friendly.
• Each other template page should have our logo discretely included in it.
• Other than the cover page, the template pages should not be too crowded with design elements. There should be lots of clear space to add material.
• I have uploaded some inspirational images that can be used to help come up with some designs.

```html
<!DOCTYPE html>
<html lang="en">
<head>
<meta charset="utf-8">
<title>Vorbelle – Presentation Template</title>
<link href="https://fonts.googleapis.com/css2?family=Open+Sans:ital,wght@0,300;0,400;0,600;0,700;1,400;1,600&display=swap" rel="stylesheet">
<style>
:root{
  --stage:#a7a9ac;
  --paper:#ffffff;
  --blue:#0255a3;
  --blue-mid:#3276b5;
  --blue-soft:#85acd3;
  --green:#9bcb3b;
  --lime:#add136;
  --green-pale:#e3eebf;
  --green-ink:#6f9a1c;
  --ink:#3b3b3b;
  --rule:#9aa3ad;
}
*{margin:0;padding:0;box-sizing:border-box}
html,body{width:1200px;height:900px;overflow:hidden}
body{background:var(--stage);font-family:'Open Sans',sans-serif;color:var(--ink);position:relative}
.slide{position:absolute;width:357px;height:276px;background:var(--paper);overflow:hidden}
.slide-title{position:absolute;left:13px;top:19px;right:13px;font-size:13px;font-weight:400;color:var(--blue);border-bottom:1px solid var(--rule);line-height:16px;padding-bottom:1px}
.wordmark{font-weight:300;color:var(--ink);letter-spacing:.5px;white-space:nowrap}
.wordmark .dot{display:inline-block;width:.42em;height:.42em;border-radius:50%;background:var(--green);margin-left:.15em;vertical-align:middle}
.slide-mark{position:absolute;left:11px;bottom:13px;font-size:12px}
.body-copy{font-size:5.4px;line-height:9.2px;color:#555;text-align:justify}
.photo{background:linear-gradient(135deg,#d7d9dc,#9a9ea4)}
.lead-accent{font-size:5.6px;line-height:9.4px;color:var(--green-ink);text-transform:uppercase}
.muted{font-size:5px;line-height:8px;color:#9a9a9a;text-align:center}
.stat{font-size:11px;font-weight:700;color:var(--blue)}
.member-name{font-size:6px;color:var(--green-ink);margin-top:10px}
.member-role{font-size:4.5px;font-style:italic;color:#555}
.slogan{font-size:9px;font-weight:400;color:var(--green-ink);letter-spacing:.4px}
</style>
</head>
<body>

<!-- Cover -->
<section class="slide" style="left:54px;top:34px;border-top:3px solid var(--blue)">
  <div class="wordmark" style="position:absolute;left:26px;top:30px;font-size:32px">Vorbelle<span class="dot"></span></div>
  <div class="slogan" style="position:absolute;left:28px;top:76px">Catalyst for innovation</div>
  <div role="img" aria-label="Green chemistry technology graphic: hydrogen peroxide molecules over a clean catalyst grid" style="position:absolute;left:0;top:97px;width:100%;height:100px;background:linear-gradient(120deg,#0255a3,#3276b5 35%,#85acd3 58%,#add136 82%,#9bcb3b)"></div>
  <div style="position:absolute;left:0;top:197px;width:100%;height:79px;background:var(--blue)"></div>
  <div style="position:absolute;left:0;top:197px;width:100%;height:3px;background:var(--green)"></div>
  <div style="position:absolute;right:20px;top:210px;text-align:right;color:#fff">
    <div style="font-size:14px;font-weight:300;line-height:17px">WELCOME</div>
    <div style="font-size:14px;font-weight:300;line-height:17px">TO OUR PRESENTATION</div>
    <div style="font-size:6.5px;margin-top:3px">Montreal, March 25, 2011</div>
  </div>
</section>

<!-- About us 1 -->
<section class="slide" style="left:424px;top:34px">
  <h2 class="slide-title">ABOUT US</h2>
  <div class="photo" role="img" aria-label="Black and white photo of a business team seated in a row" style="position:absolute;left:14px;top:40px;width:329px;height:75px"></div>
  <p class="lead-accent" style="position:absolute;left:14px;top:133px;width:105px">Lorem ipsum dolor sit met consectur adipiscing elit, sed do eiusmod tempor incididunt ut labore et delore magna</p>
  <div class="body-copy" style="position:absolute;left:134px;top:132px;width:209px">
    <p>Lorem ipsum dolor sit amet, consectetur adipisicing elit, sed do eiusmod tempor incididunt ut labore et dolore magna aliqua. Ut enim ad minim veniam, quis nostrud exercitation ullamco laboris nisi ut aliquip ex ea commodo consequat. Duis aute irure dolor in reprehenderit in voluptate velit esse cillum dolore eu fugiat nulla pariatur.</p>
    <p style="margin-top:9px">Lorem ipsum dolor sit amet, consectetur adipisicing elit, sed do eiusmod tempor incididunt ut labore et dolore magna aliqua. Ut enim ad minim veniam, quis nostrud exercitation ullamco laboris nisi ut aliquip ex ea commodo consequat. Duis aute irure dolor in reprehenderit in voluptate velit esse cillum dolore eu</p>
  </div>
  <div class="wordmark slide-mark">Vorbelle<span class="dot"></span></div>
</section>

<!-- About us 2 -->
<section class="slide" style="left:794px;top:34px">
  <h2 class="slide-title">ABOUT US</h2>
  <div style="position:absolute;left:0;top:50px;width:100%;height:69px;background:#444"></div>
  <div class="photo" role="img" aria-label="Black and white portrait of a businesswoman" style="position:absolute;left:13px;top:50px;width:94px;height:69px"></div>
  <div style="position:absolute;left:130px;top:68px;width:215px;font-size:5.8px;line-height:12.5px;color:#fff;font-style:italic;font-weight:600">Lorem ipsum dolor sit amet<br>consectetur adipisicing elit, sed do eiusmod tempor incididunt ut<br>labore et dolore magna aliqua. Ut enim ad minim veniam, quis</div>
  <div class="body-copy" style="position:absolute;left:130px;top:126px;width:214px;font-size:4.8px;line-height:7.2px">
    <p>Lorem ipsum dolor sit amet, consectetur adipisicing elit, sed do eiusmod tempor incididunt ut labore et dolore magna aliqua. Ut enim ad minim veniam, quis nostrud exercitation ullamco laboris nisi ut aliquip ex ea commodo consequat. Duis aute irure dolor in reprehenderit in voluptate velit esse cillum dolore eu fugiat nulla pariatur.</p>
    <p style="margin-top:7px">Lorem ipsum dolor sit amet, consectetur adipisicing elit, sed do eiusmod tempor incididunt ut labore et dolore magna aliqua. Ut enim ad minim veniam, quis nostrud exercitation ullamco laboris nisi ut aliquip ex ea commodo consequat. Duis aute irure dolor in reprehenderit in voluptate velit esse cillum dolore eu</p>
    <p style="margin-top:7px">fugiat nulla pariatur. Excepteur sint occaecat cupidatat non proident, sunt in culpa qui officia deserunt mollit anim id est laborum. Excepteur sint occaecat cupidatat non proident, sunt in conseq. Duis aute irure dolor in reprehenderit in voluptate velit esse cillum dolore eu</p>
  </div>
  <div class="wordmark slide-mark">Vorbelle<span class="dot"></span></div>
</section>

<!-- Chart: bars -->
<section class="slide" style="left:54px;top:318px">
  <h2 class="slide-title">OUR CHART</h2>
  <svg style="position:absolute;left:0;top:0" width="357" height="276" viewBox="0 0 357 276">
    <g stroke="#555" stroke-width=".6">
      <line x1="74" y1="48" x2="74" y2="165"/><line x1="74" y1="165" x2="290" y2="165"/>
      <line x1="71" y1="66" x2="74" y2="66"/><line x1="71" y1="86" x2="74" y2="86"/><line x1="71" y1="106" x2="74" y2="106"/><line x1="71" y1="126" x2="74" y2="126"/><line x1="71" y1="146" x2="74" y2="146"/>
      <line x1="121" y1="165" x2="121" y2="168"/><line x1="171" y1="165" x2="171" y2="168"/><line x1="221" y1="165" x2="221" y2="168"/>
    </g>
    <g>
      <rect x="81" y="79" width="11" height="86" fill="var(--blue)"/><rect x="92" y="117" width="11" height="48" fill="var(--green)"/><rect x="103" y="125" width="11" height="40" fill="var(--blue-soft)"/>
      <rect x="131" y="103" width="11" height="62" fill="var(--blue)"/><rect x="142" y="79" width="11" height="86" fill="var(--green)"/><rect x="153" y="125" width="11" height="40" fill="var(--blue-soft)"/>
      <rect x="181" y="88" width="11" height="77" fill="var(--blue)"/><rect x="192" y="127" width="11" height="38" fill="var(--green)"/><rect x="203" y="110" width="11" height="55" fill="var(--blue-soft)"/>
      <rect x="231" y="91" width="11" height="74" fill="var(--blue)"/><rect x="242" y="118" width="11" height="47" fill="var(--green)"/><rect x="253" y="82" width="11" height="83" fill="var(--blue-soft)"/>
    </g>
    <g font-size="3" fill="#fff" text-anchor="middle">
      <rect x="143" y="67" width="10" height="6" fill="var(--green-ink)"/><text x="148" y="71.5">73%</text>
      <rect x="182" y="76" width="10" height="6" fill="var(--blue)"/><text x="187" y="80.5">64%</text>
      <rect x="204" y="98" width="10" height="6" fill="var(--blue-mid)"/><text x="209" y="102.5">40%</text>
    </g>
    <g font-size="8" fill="#555" text-anchor="middle">
      <text x="98" y="182">2009</text><text x="148" y="182">2010</text><text x="198" y="182">2011</text><text x="248" y="182">2012</text>
    </g>
    <g font-size="5" fill="#444">
      <rect x="45" y="207" width="5" height="5" fill="var(--blue)"/><text x="55" y="211.5">LOREM IPSUM</text>
      <rect x="139" y="207" width="5" height="5" fill="var(--green)"/><text x="149" y="211.5">LOREM IPSUM</text>
      <rect x="233" y="207" width="5" height="5" fill="var(--blue-soft)"/><text x="244" y="211.5">LOREM IPSUM</text>
    </g>
    <g font-size="3.4" fill="#777">
      <text x="55" y="218">Lorem ipsum dolor sit amet, consectetur</text><text x="55" y="223">adipiscing elit, sed do eiusmod tempor</text><text x="55" y="228">incididunt ut labore et dolore magna</text>
      <text x="149" y="218">Lorem ipsum dolor sit amet, consectetur</text><text x="149" y="223">adipiscing elit, sed do eiusmod tempor</text><text x="149" y="228">incididunt ut labore et dolore magna</text>
      <text x="244" y="218">Lorem ipsum dolor sit amet, consectetur</text><text x="244" y="223">adipiscing elit, sed do eiusmod tempor</text><text x="244" y="228">incididunt ut labore et dolore magna</text>
    </g>
  </svg>
  <div class="wordmark slide-mark">Vorbelle<span class="dot"></span></div>
</section>

<!-- Chart: rings -->
<section class="slide" style="left:424px;top:318px">
  <h2 class="slide-title">OUR CHART</h2>
  <svg style="position:absolute;left:0;top:0" width="357" height="160" viewBox="0 0 357 160" fill="none">
    <g stroke-width="5">
      <circle cx="62" cy="103" r="25" stroke="var(--blue)"/>
      <circle cx="62" cy="103" r="25" stroke="var(--blue-soft)" stroke-dasharray="30 127" transform="rotate(-90 62 103)"/>
      <circle cx="62" cy="103" r="25" stroke="var(--green)" stroke-dasharray="12 145" transform="rotate(-5 62 103)"/>
      <circle cx="180" cy="103" r="25" stroke="var(--blue)"/>
      <circle cx="180" cy="103" r="25" stroke="var(--blue-soft)" stroke-dasharray="44 113" transform="rotate(-90 180 103)"/>
      <circle cx="180" cy="103" r="25" stroke="var(--green)" stroke-dasharray="14 143" transform="rotate(10 180 103)"/>
      <circle cx="294" cy="103" r="25" stroke="var(--blue-soft)"/>
      <circle cx="294" cy="103" r="25" stroke="var(--blue)" stroke-dasharray="40 117" transform="rotate(180 294 103)"/>
      <circle cx="294" cy="103" r="25" stroke="var(--green)" stroke-dasharray="58 99" transform="rotate(-90 294 103)"/>
    </g>
    <g fill="var(--blue)">
      <circle cx="62" cy="103" r="19"/><circle cx="180" cy="103" r="19"/><circle cx="294" cy="103" r="19"/>
    </g>
    <g fill="#fff">
      <circle cx="62" cy="103" r="7"/>
      <g stroke="#fff" stroke-width="3"><line x1="62" y1="93" x2="62" y2="113"/><line x1="52" y1="103" x2="72" y2="103"/><line x1="55" y1="96" x2="69" y2="110"/><line x1="69" y1="96" x2="55" y2="110"/></g>
      <circle cx="62" cy="103" r="3" fill="var(--blue)"/>
      <rect x="172" y="104" width="4" height="7"/><rect x="178" y="100" width="4" height="11"/><rect x="184" y="96" width="4" height="15"/>
      <path d="M170 102 l8 -6 l5 3 l7 -6" stroke="#fff" stroke-width="1.5" fill="none"/>
      <rect x="286" y="95" width="16" height="11" rx="1" fill="none" stroke="#fff" stroke-width="2"/><rect x="292" y="106" width="4" height="3"/><rect x="289" y="109" width="10" height="2"/>
    </g>
  </svg>
  <div style="position:absolute;left:17px;top:142px;width:92px;text-align:center">
    <div class="stat">81%</div>
    <p class="muted" style="margin-top:2px">dolor sit amet, consectetur adipiscing elit, sed do eiusmod tempor incididunt ut labore et dolore magna aliqua. Ut enim ad minim veniam, quis nostrud exercitation ullamco laboris nisi ut aliquip ex ea cesse cillum dolore eu fugiat nulla pariatur.</p>
  </div>
  <div style="position:absolute;left:134px;top:142px;width:92px;text-align:center">
    <div class="stat">72%</div>
    <p class="muted" style="margin-top:2px">dolor sit amet, consectetur adipiscing elit, sed do eiusmod tempor incididunt ut labore et dolore magna aliqua. Ut enim ad minim veniam, quis nostrud exercitation ullamco laboris nisi ut aliquip ex ea cesse cillum dolore eu fugiat nulla pariatur.</p>
  </div>
  <div style="position:absolute;left:248px;top:142px;width:92px;text-align:center">
    <div class="stat">63%</div>
    <p class="muted" style="margin-top:2px">dolor sit amet, consectetur adipiscing elit, sed do eiusmod tempor incididunt ut labore et dolore magna aliqua. Ut enim ad minim veniam, quis nostrud exercitation ullamco laboris nisi ut aliquip ex ea cesse cillum dolore eu fugiat nulla pariatur.</p>
  </div>
  <div class="wordmark slide-mark">Vorbelle<span class="dot"></span></div>
</section>

<!-- Team -->
<section class="slide" style="left:794px;top:318px">
  <h2 class="slide-title">OUR TEAM</h2>
  <div style="position:absolute;left:20px;top:59px;width:317px;text-align:center;font-size:5px;line-height:10px;font-style:italic;font-weight:600;color:#333">dolor sit amet, consectetur adipisicing elit, sed do eiusmod tempor incididunt ut labore et dolore magna aliqua.<br>Ut enim ad minim veniam, quis nostrud exercitation ullamco laboris nisi ut a</div>
  <div style="position:absolute;left:28px;top:84px;width:80px;text-align:center">
    <div class="photo" role="img" aria-label="Portrait of team member" style="width:52px;height:52px;border-radius:50%;margin:0 auto;border:1.5px solid var(--blue)"></div>
    <div class="member-name">JONATHAN DOE</div>
    <div class="member-role">President</div>
    <p class="muted" style="margin-top:7px;text-align:justify;line-height:10px">dolor sit amet, consectetur adipiscing elit, sed do eiusmod tempor incididunt ut labore et dolore magna aliqua. Ut enim ad minim veniam, quis nostrud exercitation</p>
  </div>
  <div style="position:absolute;left:138px;top:84px;width:80px;text-align:center">
    <div class="photo" role="img" aria-label="Portrait of team member" style="width:52px;height:52px;border-radius:50%;margin:0 auto;border:1.5px solid var(--blue)"></div>
    <div class="member-name">MELANIE DOE</div>
    <div class="member-role">CEO / Founder</div>
    <p class="muted" style="margin-top:7px;text-align:justify;line-height:10px">dolor sit amet, consectetur adipiscing elit, sed do eiusmod tempor incididunt ut labore et dolore magna aliqua. Ut enim ad minim veniam, quis nostrud exercitation</p>
  </div>
  <div style="position:absolute;left:244px;top:84px;width:80px;text-align:center">
    <div class="photo" role="img" aria-label="Portrait of team member" style="width:52px;height:52px;border-radius:50%;margin:0 auto;border:1.5px solid var(--blue)"></div>
    <div class="member-name">NATALIE DOE</div>
    <div class="member-role">Vice President</div>
    <p class="muted" style="margin-top:7px;text-align:justify;line-height:10px">dolor sit amet, consectetur adipiscing elit, sed do eiusmod tempor incididunt ut labore et dolore magna aliqua. Ut enim ad minim veniam, quis nostrud exercitation</p>
  </div>
  <div class="wordmark slide-mark">Vorbelle<span class="dot"></span></div>
</section>

<!-- Image text -->
<section class="slide" style="left:55px;top:607px;background:var(--blue)">
  <div style="position:absolute;left:15px;top:16px;font-size:12px;font-weight:300;color:#fff">IMAGE TEXT</div>
  <div style="position:absolute;left:30px;top:101px;width:137px;color:#fff">
    <div style="font-size:5.6px;margin-bottom:7px">LOREM IPSUM DOLOR SIT MET</div>
    <p class="body-copy" style="color:#e6eef8;font-size:4.8px;line-height:7.2px">Lorem ipsum dolor sit amet, consectetur adipiscing elit, sed do eiusmod tempor incididunt ut labore et dolore magna aliqua. Ut enim ad minim veniam, quis nostrud exercitation ullamco laboris nisi ut aliquip ex ea commodo consequat. Duis aute irure dolor in reprehenderit in voluptate velit esse cillum dolore eu fugiat nulla pariatur.</p>
    <p class="body-copy" style="color:#e6eef8;font-size:4.8px;line-height:7.2px;margin-top:7px">Lorem ipsum dolor sit amet, consectetur adipiscing elit, sed do eiusmod tempor incididunt ut labore et dolore magna aliqua. Ut enim ad minim veniam, quis nostrud exercitation ullamco laboris nisi ut aliquip ex ea commodo consequat. Duis aute irure dolor in reprehenderit in voluptate velit esse cillum dolore eu</p>
  </div>
  <div class="wordmark" style="position:absolute;left:13px;bottom:17px;font-size:11px;color:var(--blue-mid)">Vorbelle</div>
  <div class="photo" role="img" aria-label="Black and white photo of a smiling young woman and man" style="position:absolute;left:182px;top:0;width:175px;height:276px;background:linear-gradient(160deg,#f1f1f1,#9d9d9d)"></div>
</section>

<!-- Section title -->
<section class="slide" style="left:424px;top:607px;background:linear-gradient(135deg,#0255a3,#3276b5 45%,#85acd3 75%,#9bcb3b)">
  <div role="img" aria-label="Faint molecular structure illustration" style="position:absolute;inset:0;background:radial-gradient(circle at 30% 40%,rgba(255,255,255,.14),transparent 55%)"></div>
  <svg style="position:absolute;left:154px;top:120px" width="48" height="48" viewBox="0 0 48 48">
    <circle cx="24" cy="24" r="23" fill="#fff"/>
    <circle cx="27" cy="12" r="4" fill="var(--green-ink)"/>
    <path d="M19 21 h9 l-5 16 h4 l-1 3 h-10 l1-3 h2 l4-13 h-5z" fill="var(--green-ink)"/>
  </svg>
  <div style="position:absolute;left:122px;top:174px;width:113px;border-top:1px solid rgba(255,255,255,.8)"></div>
  <div style="position:absolute;left:0;width:100%;top:180px;text-align:center;font-size:11px;font-weight:300;color:#fff">SECTION TITLE</div>
</section>

<!-- Contact -->
<section class="slide" style="left:792px;top:610px;height:275px">
  <div class="wordmark" style="position:absolute;left:24px;top:26px;font-size:32px">Vorbelle<span class="dot"></span></div>
  <div role="img" aria-label="Street map of the office neighbourhood with a location pin" style="position:absolute;left:0;top:91px;width:100%;height:107px;background:linear-gradient(100deg,#eef2e2,#e3eebf 55%,#d5e6a6)"></div>
  <div style="position:absolute;left:0;top:198px;width:100%;height:77px;background:var(--blue)"></div>
  <svg style="position:absolute;left:0;top:190px" width="357" height="10"><polygon points="240,8 250,0 357,0 357,8" fill="var(--green)"/></svg>
  <div style="position:absolute;left:30px;top:211px;color:#fff;font-size:5.4px;line-height:7px">
    <div style="display:flex;gap:6px;align-items:flex-start"><svg width="9" height="9" viewBox="0 0 10 10"><circle cx="5" cy="5" r="5" fill="#fff"/><path d="M5 2a2 2 0 0 1 2 2c0 1.5-2 4-2 4S3 5.5 3 4a2 2 0 0 1 2-2z" fill="var(--blue)"/></svg><span>410 Rue Lenoir Ste 12<br>Montreal, QC H4C 1Y3</span></div>
    <div style="display:flex;gap:6px;align-items:center;margin-top:7px"><svg width="9" height="9" viewBox="0 0 10 10"><circle cx="5" cy="5" r="5" fill="#fff"/><path d="M3 3h1.5l.5 1.5-1 .6a4 4 0 0 0 1.9 1.9l.6-1L8 6.5V8C5 8 2 5 2 3z" fill="var(--blue)"/></svg><span>1.800.555.0142</span></div>
    <div style="display:flex;gap:6px;align-items:center;margin-top:8px"><svg width="9" height="9" viewBox="0 0 10 10"><circle cx="5" cy="5" r="5" fill="#fff"/><rect x="3" y="2.5" width="4" height="5" rx=".6" fill="var(--blue)"/></svg><span>514.555.0187</span></div>
  </div>
  <div style="position:absolute;left:168px;top:211px;color:#fff;font-size:5.4px;line-height:7px">
    <div style="display:flex;gap:6px;align-items:center"><svg width="9" height="9" viewBox="0 0 10 10"><circle cx="5" cy="5" r="5" fill="#fff"/><rect x="2.5" y="3.2" width="5" height="3.6" fill="none" stroke="var(--blue)" stroke-width=".8"/><path d="M2.5 3.2l2.5 2 2.5-2" fill="none" stroke="var(--blue)" stroke-width=".8"/></svg><span>support@vorbelle-tech.com</span></div>
    <div style="display:flex;gap:6px;align-items:center;margin-top:10px"><svg width="9" height="9" viewBox="0 0 10 10"><circle cx="5" cy="5" r="5" fill="#fff"/><circle cx="5" cy="5" r="3" fill="none" stroke="var(--blue)" stroke-width=".7"/><line x1="2" y1="5" x2="8" y2="5" stroke="var(--blue)" stroke-width=".7"/></svg><span>www.vorbelle-tech.com</span></div>
    <div style="display:flex;gap:3px;margin-top:10px"><span style="width:9px;height:9px;background:#fff;border-radius:1.5px"></span><span style="width:9px;height:9px;background:#fff;border-radius:1.5px"></span><span style="width:9px;height:9px;background:#fff;border-radius:1.5px"></span></div>
  </div>
</section>

<!-- shared footers for template pages -->
<svg style="position:absolute;left:0;top:0;pointer-events:none" width="1200" height="900">
  <defs>
    <g id="footer-bar">
      <rect x="0" y="0" width="357" height="5" fill="#3d3d3d"/>
      <polygon points="255,5 262,0 357,0 357,5" fill="var(--blue)"/>
      <polygon points="248,5 255,0 262,0 255,5" fill="var(--green)"/>
      <text x="350" y="4.2" font-size="4" fill="#fff" font-family="Open Sans,sans-serif">2</text>
    </g>
  </defs>
  <use href="#footer-bar" x="424" y="305"/>
  <use href="#footer-bar" x="794" y="305"/>
  <use href="#footer-bar" x="54" y="589"/>
  <use href="#footer-bar" x="424" y="589"/>
  <use href="#footer-bar" x="794" y="589"/>
</svg>

</body>
</html>
```